Business Card Design

We would like a business card that utilizes our current logo and keeps with the same feel - elegant and organic. Our farm isn't about mass production, it's about excellence, education, beautiful events and flowers - people, culture, and community.

Target Market(s)

Patrons to our farm who are interested in weddings, events, or our flowers and vegetables.

Contact Information for Business Card

Name, address, cell email (Danielle Hoskins, 2716 Wrenfield Rd, Larkhaven, CO 80611, cell 30.412.6638, email danielle@wrenfieldacres.com)

```html
<!DOCTYPE html>
<html lang="en">
<head>
<meta charset="utf-8">
<title>Wrenfield Acres – Business Card</title>
<link href="https://fonts.googleapis.com/css2?family=Poppins:wght@500;600&family=Arimo:wght@400&display=swap" rel="stylesheet">
<style>
  :root {
    --backdrop: #c1b8b9;
    --sage: #788a77;
    --paper: #ffffff;
    --ink: #2f2f2f;
    --rule: #b9bdb8;
    --ghost-light: rgba(120, 120, 120, 0.08);
    --ghost-dark: rgba(70, 90, 70, 0.20);
  }
  * { margin: 0; padding: 0; box-sizing: border-box; }
  html, body { width: 1065px; height: 1200px; overflow: hidden; }
  body { background: var(--backdrop); position: relative; font-family: "Arimo", Arial, sans-serif; }

  .card { position: absolute; width: 583px; height: 362px; overflow: hidden; }
  .card--front { left: 292px; top: 218px; background: var(--paper); border-radius: 0 181px 181px 0; }
  .card--back { left: 263px; top: 623px; background: var(--sage); border-radius: 181px 0 0 181px; }

  .ghost-name {
    position: absolute; font-family: "Poppins", sans-serif; font-weight: 500;
    font-size: 58px; letter-spacing: 1px; white-space: nowrap; line-height: 1;
  }
  .card--front .ghost-name { color: var(--ghost-light); left: 24px; top: 236px; }
  .card--back .ghost-name { color: var(--ghost-dark); left: 50px; top: 222px; }

  .brand-vertical {
    position: absolute; left: 125px; top: 181px; transform: translate(-50%, -50%) rotate(-90deg);
    font-family: "Poppins", sans-serif; font-weight: 500; font-size: 28px; color: var(--sage);
    white-space: nowrap; letter-spacing: 1px;
  }
  .divider { position: absolute; left: 202px; top: 99px; width: 1px; height: 166px; background: var(--rule); }

  .contact { position: absolute; left: 230px; top: 96px; color: var(--ink); }
  .contact__name {
    font-family: "Poppins", sans-serif; font-weight: 600; font-size: 21px;
    color: var(--sage); letter-spacing: 0.2px; margin-bottom: 16px;
  }
  .contact__line { display: flex; align-items: center; gap: 5px; font-size: 16.5px; height: 21.5px; }
  .contact__line svg { width: 15px; height: 15px; fill: var(--sage); flex: none; }
  .contact__line .accent { color: var(--sage); }
  .contact__address { margin-top: 20px; font-size: 16.5px; line-height: 21.5px; }

  .brand-center {
    position: absolute; left: 50%; top: 50%; transform: translate(-50%, -50%);
    font-family: "Poppins", sans-serif; font-weight: 500; font-size: 34px; color: var(--paper);
    white-space: nowrap; letter-spacing: 1px;
  }
</style>
</head>
<body>
  <section class="card card--front">
    <div class="ghost-name" aria-hidden="true">Wrenfield Acres</div>
    <div class="brand-vertical">Wrenfield Acres</div>
    <div class="divider"></div>
    <div class="contact">
      <h1 class="contact__name">DANIELLE HOSKINS</h1>
      <p class="contact__line">
        <svg viewBox="0 0 24 24" aria-hidden="true"><path d="M6.6 10.8a15.1 15.1 0 0 0 6.6 6.6l2.2-2.2c.3-.3.7-.4 1-.2 1.1.4 2.3.6 3.6.6.6 0 1 .4 1 1V20c0 .6-.4 1-1 1A17 17 0 0 1 3 4c0-.6.4-1 1-1h3.5c.6 0 1 .4 1 1 0 1.3.2 2.5.6 3.6.1.3 0 .7-.2 1z"/></svg>
        30.412.6638
      </p>
      <p class="contact__line">
        <svg viewBox="0 0 24 24" aria-hidden="true"><path d="M2 5h20v14H2z"/><path d="M2 6l10 8 10-8" fill="none" stroke="#fff" stroke-width="1.6"/></svg>
        danielle@wrenfieldacres.com
      </p>
      <p class="contact__line">
        <svg viewBox="0 0 24 24" aria-hidden="true"><path d="M12 2a10 10 0 1 0 0 20 10 10 0 0 0 0-20zm0 2c.9 0 2.2 2 2.7 5H9.3C9.8 6 11.1 4 12 4zM4.3 10h3c-.1.7-.1 1.3-.1 2s0 1.3.1 2h-3a8 8 0 0 1 0-4zm1 6h2.3c.3 1.3.8 2.5 1.4 3.4A8 8 0 0 1 5.3 16zm2.3-8H5.3A8 8 0 0 1 9 4.6C8.4 5.5 7.9 6.7 7.6 8zM12 20c-.9 0-2.2-2-2.7-4h5.4c-.5 2-1.8 4-2.7 4zm2.9-6H9.1c-.1-.6-.1-1.3-.1-2s0-1.4.1-2h5.8c.1.6.1 1.3.1 2s0 1.4-.1 2zm.1 5.4c.6-.9 1.1-2.1 1.4-3.4h2.3a8 8 0 0 1-3.7 3.4zM16.7 14c.1-.7.1-1.3.1-2s0-1.3-.1-2h3a8 8 0 0 1 0 4zm-.3-6c-.3-1.3-.8-2.5-1.4-3.4A8 8 0 0 1 18.7 8z"/></svg>
        <span>www.<span class="accent">wrenfieldacres</span>.com</span>
      </p>
      <p class="contact__address">2716 Wrenfield Rd, Larkhaven<br>CO 80611</p>
    </div>
  </section>

  <section class="card card--back">
    <div class="ghost-name" aria-hidden="true">Wrenfield Acres</div>
    <div class="brand-center">Wrenfield Acres</div>
  </section>
</body>
</html>
```